Restaurant Needs a Flyer Design for a Cocktail Competition

We are a Chinese restaurant specializing in hot pot cuisine. More information about our specialty and product line can be found on our website: www.brinskaleto.com.
We are expanding our bar menu and plan to hold a competition between local bartenders to craft new signature sake cocktails for our restaurant. We need someone to design a flyer that can be distributed to local bars and restaurants in order to catch their interest.
For the name of the competition, we were considering something along the lines of "Season of Sake - Brinska Leto's Cocktail Competition". However, more consideration will be given to designs that come up with an original, creative headline. The headline must reference that it is a "sake cocktail" competition to avoid any confusion.
The overall look of the flyer should be fun and eye-catching.
The information that we need included on the front of the flyer (not in this wording or order) is as follows:
1. Name of our restaurant, website, and location
2. The name of the competition
3. Submissions must be submitted to this email address: brinskaleto1@mailvane.com
4. The deadline for submissions is July 31st, 2015
5. Images to accompany the text as well as our logo
6. Eight finalists will be chosen by the restaurant's staff and the top three will be chosen by customer vote.
7. The top three will be awarded prizes:
a. Grand Prize Winner: The choice of either a
"Winner's Dinner" for them and their entire staff
OR a cash prize of $300
b. 2nd Prize Winner: $100 cash prize AND $100
Brinska Leto gift card
c. 3rd Prize Winner: $100 Brinska Leto gift card
8. ALL three winners will receive a credit under their winning drink on our menu - their bar/restaurant will be credited on the menu as well
9. The eight finalists will be chosen by August 10th, 2015 and the three winners will be chosen by August 31st, 2015.
On the back of the flyer we will include a list of our submission guidelines and contest rules. Those guidelines and rules are included as attachments at the bottom along with our logo.

```html
<!DOCTYPE html>
<html lang="en">
<head>
<meta charset="utf-8">
<title>Season of Sake – Brinska Leto's Cocktail Competition Flyer</title>
<link href="https://fonts.googleapis.com/css2?family=Questrial&family=Cabin:wght@400;600;700&display=swap" rel="stylesheet">
<style>
:root{
  --bg:#e4e5e7;
  --red:#c4201d;
  --dark-red:#5b0808;
  --green:#6aac22;
  --yellow:#f4e04a;
  --white:#ffffff;
  --ink:#333333;
  --grey-bar:#e3e3e3;
  --tick:#6aac22;
}
*{margin:0;padding:0;box-sizing:border-box}
html,body{width:1200px;height:1000px;overflow:hidden;background:var(--bg)}
body{position:relative;font-family:"Cabin",sans-serif;color:var(--ink)}
.page{position:absolute;top:160px;width:476px;height:673px;background:var(--white);overflow:hidden;box-shadow:0 2px 6px rgba(0,0,0,.15)}
.page--front{left:108px}
.page--back{left:618px}
.header{position:absolute;left:0;top:0;width:100%}
.header svg{display:block}
.brand{position:absolute;left:22px;top:12px;font-family:"Questrial",sans-serif;font-size:40px;color:var(--white);letter-spacing:1px}
.contest-title{position:absolute;left:0;width:100%;text-align:center;font-family:"Questrial",sans-serif;color:var(--white);font-size:18px}
.page--front .contest-title{top:64px}
.page--back .contest-title{top:57px}
.submit-note{position:absolute;color:var(--yellow);font-size:12px;font-weight:600;line-height:15px}
.submit-note span{color:var(--white)}
.page--front .submit-note{left:25px;top:91px;width:225px}
.page--back .submit-note{left:26px;top:81px;width:440px}
.photo{position:absolute;z-index:1;background:var(--white);padding:4px;box-shadow:0 1px 4px rgba(0,0,0,.35)}
.photo div{width:100%;height:100%}
.photo--hotpot{left:268px;top:96px;width:216px;height:150px;transform:rotate(-3deg)}
.photo--hotpot div{background:linear-gradient(135deg,#c9b58a,#a0753e 45%,#c3442a 80%,#e0d6c0)}
.photo--chicken{left:270px;top:246px;width:212px;height:140px;transform:rotate(2deg)}
.photo--chicken div{background:linear-gradient(135deg,#7a3f1a,#b8622a 50%,#6a8a34)}
.photo--skewer{left:252px;top:380px;width:232px;height:155px;transform:rotate(-2deg)}
.photo--skewer div{background:linear-gradient(135deg,#f0ece2,#d8b07a 50%,#9b6a38)}
.deadline-badge{position:absolute;z-index:2;left:186px;top:122px;width:138px;height:138px}
.deadline-badge svg{display:block}
.deadline-badge p{position:absolute;left:0;top:36px;width:100%;text-align:center;color:var(--white);font-family:"Questrial",sans-serif;font-size:12px;line-height:15px;transform:rotate(-12deg)}
.deadline-badge strong{display:block;color:var(--yellow);font-size:19px;font-weight:400;line-height:22px}
.finalists{position:absolute;left:10px;top:168px;width:192px;text-align:center;font-family:"Questrial",sans-serif;font-size:14.5px;line-height:19px;color:#222}
.finalists .hl{color:var(--red);font-size:16px}
.section-bar{position:absolute;height:27px;background:var(--grey-bar);font-family:"Cabin",sans-serif;font-size:13px;font-weight:600;line-height:27px;padding-left:12px;color:#222}
.page--front .section-bar{left:15px;top:285px;width:258px}
.prizes{position:absolute;left:18px;top:326px;width:232px;list-style:none;font-size:9.5px;line-height:12.5px}
.prizes li{position:relative;padding-left:15px;margin-bottom:11px}
.prizes li::before{content:"";position:absolute;left:1px;top:2px;width:4px;height:7px;border:solid #222;border-width:0 1.5px 1.5px 0;transform:rotate(45deg)}
.prizes .label{color:var(--red);font-weight:600}
.prizes .accent{color:var(--green);font-weight:600}
.credit-box{position:absolute;left:20px;top:438px;width:222px;height:102px;background:var(--dark-red);border-radius:4px;color:var(--white);text-align:center;font-size:12px;font-weight:600;line-height:18px;padding:14px 10px 0}
.dates{position:absolute;left:20px;top:560px;width:436px;text-align:center;font-family:"Questrial",sans-serif;font-size:13px;line-height:18px;color:#222}
.dates strong{font-weight:700}
.footer{position:absolute;left:0;bottom:0;width:100%;height:60px;background:var(--green);color:var(--white);text-align:center;font-size:9.5px;line-height:17px;padding-top:13px}
.footer b{color:var(--yellow);font-weight:400}
.footer .gap{display:inline-block;width:18px}
.page--back .section-bar{left:15px;width:268px}
.bar--rules{top:141px}
.bar--guidelines{top:390px}
.rules{position:absolute;left:18px;width:420px;list-style:none;font-size:8.6px;line-height:11.5px;color:#444}
.rules > li{position:relative;padding-left:14px;margin-bottom:9.5px}
.rules > li::before{content:"";position:absolute;left:2px;top:1px;width:4px;height:7px;border:solid var(--tick);border-width:0 1.5px 1.5px 0;transform:rotate(45deg)}
.rules--contest{top:180px}
.rules--contest li.narrow{width:282px}
.rules--guidelines{top:430px;width:282px}
.rules--guidelines ul{list-style:none;margin-top:3px}
.rules--guidelines ul li{position:relative;padding-left:10px;margin-bottom:3px}
.rules--guidelines ul li::before{content:"";position:absolute;left:3px;top:4px;width:3px;height:3px;border-radius:50%;background:#444}
.mascot{position:absolute;left:308px;top:335px;width:150px;height:275px;border-radius:70px 70px 20px 20px;background:linear-gradient(180deg,#e8e3da 0%,#f0a36a 40%,#e26a1e 60%,#3a3a3a 82%,#e8421d 100%)}
</style>
</head>
<body>

<section class="page page--front" aria-label="Flyer front">
  <div class="header">
    <svg width="476" height="170" viewBox="0 0 476 170" aria-hidden="true">
      <polygon fill="var(--red)" points="0,0 476,0 476,130 460,133 440,128 420,134 400,129 380,135 360,130 340,136 320,131 300,137 280,133 260,139 240,134 220,140 200,136 180,143 160,138 140,144 120,139 100,146 80,141 60,147 40,142 20,148 0,145"/>
    </svg>
    <div class="brand">Brinska Leto</div>
    <div class="contest-title">“ Season of Sake - Brinska Leto's Cocktail Competition ”</div>
    <p class="submit-note">Submissions must be submitted to this email address : <span>brinskaleto1@mailvane.com</span></p>
  </div>

  <figure class="photo photo--hotpot"><div role="img" aria-label="Photo of a hot pot with side dishes and sauces"></div></figure>
  <figure class="photo photo--chicken"><div role="img" aria-label="Photo of a stir-fried chicken dish"></div></figure>
  <figure class="photo photo--skewer"><div role="img" aria-label="Photo of grilled chicken skewers"></div></figure>

  <div class="deadline-badge">
    <svg width="138" height="138" viewBox="0 0 128 128" aria-hidden="true">
      <polygon fill="var(--green)" points="64,2 74,14 89,7 94,22 110,22 109,38 124,45 116,59 126,72 113,81 117,97 101,100 97,116 82,112 72,125 62,115 49,124 42,110 26,112 25,96 10,90 17,76 5,64 17,54 12,38 28,34 30,18 46,21 53,6"/>
    </svg>
    <p>The deadline<br>for submissions is<strong>July 31st,<br>2015</strong></p>
  </div>

  <p class="finalists"><span class="hl">EIGHT FINALISTS</span><br>will be chosen by the restaurant's staff and the top three will be chosen<br><span class="hl">by customer vote.</span></p>

  <div class="section-bar">The top three will be awarded prizes:</div>
  <ul class="prizes">
    <li><span class="label">Grand Prize Winner:</span> The choice of either a "Winner's Dinner" for them and their <span class="accent">entire staff OR a cash prize of $300</span></li>
    <li><span class="label">2nd Prize Winner:</span> $100 cash prize AND $100 Brinska Leto gift card</li>
    <li><span class="label">3rd Prize Winner:</span> $100 Brinska Leto gift card</li>
  </ul>

  <div class="credit-box">ALL three winners will receive a credit under their winning drink on our menu - their bar/restaurant will be credited on the menu as well</div>

  <p class="dates">The eight finalists will be chosen by August 10th, 2015 and the three winners will be chosen by <strong>August 31st, 2015.</strong></p>

  <footer class="footer">
    <b>LOCATION -</b> 418 Corvel Avenue Suite 12, Lake Harlow, FL 32700<br>
    <b>PHONE -</b> (407) 555-0142<span class="gap"></span><b>WEBSITE -</b> www.brinskaleto.com
  </footer>
</section>

<section class="page page--back" aria-label="Flyer back">
  <div class="header">
    <svg width="476" height="140" viewBox="0 0 476 140" aria-hidden="true">
      <polygon fill="var(--red)" points="0,0 476,0 476,122 456,126 436,121 416,128 396,123 376,129 356,124 336,130 316,125 296,131 276,126 256,132 236,127 216,133 196,128 176,134 156,129 136,135 116,130 96,136 76,131 56,137 36,132 16,138 0,134"/>
    </svg>
    <div class="brand">Brinska Leto</div>
    <div class="contest-title">“ Season of Sake - Brinska Leto's Cocktail Competition ”</div>
    <p class="submit-note">Submissions must be submitted to this email address : <span>brinskaleto1@mailvane.com</span></p>
  </div>

  <div class="section-bar bar--rules">Contest Rules</div>
  <ul class="rules rules--contest">
    <li>Winning recipes will become the property of Brinska Leto and cannot be duplicated or resold anywhere else - winners will be credited on the menu</li>
    <li>All cocktail recipes MUST be original – be creative!</li>
    <li>Any ingredients will be considered; however, sake is a key component and there can be no ingredient with an alcohol content above 20%</li>
    <li>Top eight finalists will be contacted via email and phone on August 10th, 2015. If they do not respond with 48 hours, another finalist will be chosen in their place.</li>
    <li>From August 11th, 2015 - August 31st, 2015, voting for the three winners will take place in Brinska Leto's restaurant. The three cocktails that receive the most votes from our customers will be chosen for the 1st, 2nd, and 3rd prizes.</li>
    <li class="narrow">The final three winners will be contacted on August 31st, 2015. If they do not respond with 48 hours, the finalist with the next highest amount of votes will be chosen in their place.</li>
  </ul>

  <div class="section-bar bar--guidelines">Submission Guidelines</div>
  <ul class="rules rules--guidelines">
    <li>Please include the following information:
      <ul>
        <li>Name of the cocktail</li>
        <li>Ingredients List and Measurements</li>
        <li>Detailed list of instructions</li>
        <li>Photo of the cocktail</li>
        <li>Any specific equipment/materials or glassware, if necessary</li>
        <li>Your name, the name of your restaurant, and the best way to contact you</li>
      </ul>
    </li>
    <li>Submit all materials to brinskaleto1@mailvane.com - in the subject line include your name and the name of your cocktail</li>
    <li>If you have any questions, please contact us via email or our store number: 407-555-0142.</li>
  </ul>

  <div class="mascot" role="img" aria-label="Cartoon illustration of a cook eating noodles over a hot pot on a flame"></div>

  <footer class="footer">
    <b>LOCATION -</b> 418 Corvel Avenue Suite 12, Lake Harlow, FL 32700<br>
    <b>PHONE -</b> (407) 555-0142<span class="gap"></span><b>WEBSITE -</b> www.brinskaleto.com
  </footer>
</section>

</body>
</html>
```